Bourbon label design for bourbon brand. Looking to freshen our current label.

I need a Bourbon label design for our rebranded Bourbon bottle. Label should include picture of our horse and our logo on the bottle. Front Label is 3.5 inches wide and 6 inches tall, back label is 4 inches tall and 3 inches wide. Back label can be a simple plain logo like the one in the brief. I have included a design of our current bottle and label. We want to stay close to the current color schemes but want a fresh rebrand of the design. The label needs to be the correct size on a tall bottle like pictured.

Target Market(s)

Our Bourbon members, 30-50 year old males

Requirements
Must have
• Picture of our horse, our B logo , straight Bourbon whiskey on the front. Room to edit text on the back label.

```html
<!DOCTYPE html>
<html lang="en">
<head>
<meta charset="utf-8">
<title>Champions Series – Silver Gale Edition Labels</title>
<link href="https://fonts.googleapis.com/css2?family=Cinzel:wght@500;700&family=Montserrat:wght@400;500;700&display=swap" rel="stylesheet">
<style>
  :root {
    --page: #ffffff;
    --label: #070808;
    --ink: #ffffff;
    --ink-soft: #e6e6e6;
    --sketch-hi: #5a5a5a;
    --sketch-lo: #161616;
  }
  * { box-sizing: border-box; margin: 0; padding: 0; }
  html, body { width: 806px; height: 1200px; overflow: hidden; background: var(--page); }
  .canvas { position: relative; width: 806px; height: 1200px; }

  .label {
    position: absolute; top: 398px; width: 269px; height: 404px;
    background: var(--label); color: var(--ink); text-align: center;
  }
  .label--back { left: 113px; }
  .label--front { left: 424px; }
  .label > * { position: absolute; left: 0; right: 0; }

  .brand {
    top: 14px; display: flex; flex-direction: column; align-items: center; gap: 3px;
    font-family: "Montserrat", sans-serif; font-weight: 700; color: var(--ink);
  }
  .brand__mark { width: 16px; height: 16px; border-radius: 50%; background: var(--ink); margin-bottom: 3px; }
  .brand__name { font-size: 7.5px; line-height: 1.05; letter-spacing: .3px; }

  .title { font-family: "Cinzel", serif; }
  .title__series { font-size: 18.5px; font-weight: 700; letter-spacing: .2px; line-height: 1; }
  .title__edition { font-size: 9.6px; font-weight: 700; margin-top: 4px; letter-spacing: .3px; }
  .title__barrel { font-size: 6.6px; font-weight: 700; margin-top: 3px; letter-spacing: .2px; }
  .label--back .title { top: 89px; }
  .label--front .title { top: 317px; }

  .story {
    top: 149px; left: 24px; right: 24px;
    font-family: "Cinzel", serif; font-weight: 700; font-size: 6.6px; line-height: 1.36;
  }
  .story p + p { margin-top: 9px; }

  .producer {
    top: 240px; left: 26px; right: 25px; height: 57px;
    border: 0.8px solid var(--ink-soft); padding-top: 13px;
  }
  .producer__line { font-family: "Cinzel", serif; font-weight: 700; font-size: 5.6px; line-height: 1.3; }
  .producer__web { font-family: "Montserrat", sans-serif; font-weight: 500; font-size: 10.2px; margin-top: 6px; }

  .warning {
    top: 310px; left: 22px; right: 22px;
    font-family: "Montserrat", sans-serif; font-size: 5.9px; line-height: 1.32; color: var(--ink-soft);
  }
  .warning strong { font-weight: 700; color: var(--ink); }

  .volume { top: 376px; font-family: "Montserrat", sans-serif; font-size: 10.5px; font-weight: 400; }

  .horse-art {
    top: 95px; left: 51px; right: 33px; height: 202px; border-radius: 4px;
    background: radial-gradient(ellipse at 50% 45%, var(--sketch-hi) 0%, #2a2a2a 45%, var(--sketch-lo) 80%, var(--label) 100%);
  }
</style>
</head>
<body>
<main class="canvas">

  <section class="label label--back" aria-label="Back label">
    <div class="brand">
      <span class="brand__mark"></span>
      <span class="brand__name">NIGHTFALL<br>CASK COMPANY</span>
    </div>
    <div class="title">
      <h1 class="title__series">CHAMPIONS SERIES</h1>
      <h2 class="title__edition">SILVER GALE EDITION</h2>
      <p class="title__barrel">SINGLE BARREL NO.45</p>
    </div>
    <div class="story">
      <p>THE NIGHTFALL RACING CHAMPIONS SERIES HONORS THE HORSES WHO HAVE BROUGHT HOME VICTORIES FOR OUR STABLE. THIS EDITION CELEBRATES SILVER GALE AND HER MAIDEN VICTORY ON MAY 28, 2021.</p>
      <p>RAISE A GLASS TO HER INCREDIBLE CAREER WITH THIS NON-CHILL FILTERED SINGLE BARREL CRAFTED IN HER HONOR. HERE'S TO SILVER GALE—A TRUE CHAMPION!</p>
    </div>
    <div class="producer">
      <p class="producer__line">BOTTLED BY RIVERBEND WHISKEY CO., LOUISVILLE, KENTUCKY<br>DISTILLED IN BARDSTOWN, KENTUCKY</p>
      <p class="producer__web">nightfall-group.example</p>
    </div>
    <p class="warning"><strong>GOVERNMENT WARNING:</strong> (1) According to the Surgeon General, women should not drink alcoholic beverages during pregnancy because of the risk of birth defects. (2) Consumption of alcoholic beverages impairs your ability to drive a car or operate machinery, and may cause health problems.</p>
    <p class="volume">750 ml</p>
  </section>

  <section class="label label--front" aria-label="Front label">
    <div class="brand">
      <span class="brand__mark"></span>
      <span class="brand__name">NIGHTFALL<br>CASK COMPANY</span>
    </div>
    <div class="horse-art" role="img" aria-label="White pen sketch of a jockey riding a galloping racehorse"></div>
    <div class="title">
      <h1 class="title__series">CHAMPIONS SERIES</h1>
      <h2 class="title__edition">SILVER GALE EDITION</h2>
      <p class="title__barrel">SINGLE BARREL NO.45</p>
    </div>
    <p class="volume">750 ml</p>
  </section>

</main>
</body>
</html>
```